Wireless Internet Service Provider website design

We need a Internet Service Provider website that show the packages that we offer as well as the functionality where customers have the option of clicking on the various packages and be linked to a page where they can sign up for our services.
We need about 10-15 pages.
A. Integrated online store.
B. Live chat.
C. Social media page
My old website. Brightlinknet.nyc

Example: http://pinecrestlink.com/services/residential/ Added Tuesday, June 7, 2016

Target Market(s)

Residential and small businesses

Industry/Entity Type

Internet

Coding

Coded - Design and coding required

Number of Pages Required

5+ page

Font styles to use
Serif
Sans Serif
Script

Colors
3176b5
85cae6
ffffff

Requirements
Must have
• Online store and live chat, drop down details on pricing from current website
Nice to have
• great design, functional website,

```html
<!DOCTYPE html>
<html lang="en">
<head>
<meta charset="utf-8">
<title>Brightlink – Wireless Internet</title>
<link href="https://fonts.googleapis.com/css2?family=Hind:wght@400;500;600&family=Open+Sans:wght@400;600;700&display=swap" rel="stylesheet">
<style>
:root{
  --blue:#0f5fa6;
  --blue-dark:#0b4f8f;
  --teal:#1bb1cc;
  --teal-light:#85cae6;
  --ink:#1c1c1c;
  --grey-text:#666;
  --panel:#efefef;
  --footer:#1c1c1c;
  --footer-deep:#141414;
  --white:#fff;
}
*{box-sizing:border-box;margin:0;padding:0}
html,body{width:1200px;height:3734px;overflow:hidden}
body{font-family:"Open Sans",Arial,sans-serif;color:var(--ink);background:var(--white);position:relative}
.abs{position:absolute}
h2.section-title{font-family:"Hind",Arial,sans-serif;font-weight:500;text-align:center;font-size:40px;letter-spacing:1px}
.section-sub{text-align:center;font-size:13px;color:var(--grey-text);margin-top:6px}

/* hero */
.hero{left:0;top:0;width:1200px;height:727px;background:linear-gradient(120deg,#d9dde2 0%,#b7c0c9 40%,#8b96a2 70%,#c9ced3 100%)}
.logo-box{left:38px;top:25px;width:230px;height:120px;background:var(--white);display:flex;align-items:center;gap:12px;padding-left:22px}
.logo-mark{width:36px;height:36px;background:var(--teal)}
.logo-name{font-family:"Open Sans",Arial,sans-serif;font-weight:600;font-size:24px;color:var(--blue)}
.nav-bar{left:268px;top:25px;width:875px;height:120px;background:var(--blue)}
.nav-top{position:absolute;right:20px;top:14px;display:flex;gap:14px;align-items:center;color:var(--white);font-size:15px}
.dot{width:24px;height:24px;border-radius:50%;background:var(--white)}
.nav-links{position:absolute;left:86px;top:62px;display:flex;gap:6px;align-items:center}
.nav-links a{color:var(--white);font-size:14px;text-decoration:none;padding:12px 14px;font-weight:600}
.nav-links a.active{background:var(--teal)}
.signup-btn{background:var(--teal);color:var(--white);font-size:15px;padding:10px 14px;display:flex;gap:8px;align-items:center;margin-left:6px}
.hero-box{left:62px;top:331px;width:580px;height:174px;background:var(--teal);padding:22px 26px;color:var(--white)}
.hero-box h1{font-family:"Hind",Arial,sans-serif;font-weight:600;font-size:38px;line-height:42px;letter-spacing:1px}
.hero-box p{font-size:15px;margin-top:16px}

/* why */
.why{left:0;top:786px;width:1200px}
.card{top:924px;width:247px;height:321px;background:var(--panel);text-align:center}
.card-photo{height:108px;background:linear-gradient(180deg,#3f8fd6,#8dbfe6 60%,#7a6f63)}
.card-label{height:40px;background:var(--blue);color:var(--white);font-size:15px;line-height:40px}
.card p{font-size:12.5px;color:#444;padding:14px 18px 0;line-height:17px;height:96px}
.btn{display:inline-block;background:var(--teal);color:var(--white);font-size:12px;font-weight:600;padding:9px 14px}

/* speed */
.speed-photo{left:0;top:1330px;width:590px;height:463px;background:linear-gradient(135deg,#6a5a4c,#9c8b7d 45%,#4d5a63)}
.speed-panel{left:590px;top:1330px;width:610px;height:463px;background:var(--panel);padding:30px 30px 0 28px}
.speed-panel h2{font-family:"Hind",Arial,sans-serif;font-weight:500;font-size:34px;line-height:38px}
.rule{width:80px;height:4px;background:var(--teal);margin:8px 0 22px}
.speed-panel p{font-size:13px;color:var(--grey-text);line-height:22px;margin-bottom:14px}
.features{display:flex;gap:26px;margin:4px 0 18px}
.feature{display:flex;gap:10px;align-items:center;color:#1d3f6e;font-size:16px;line-height:20px}
.speed-btn{display:inline-block;background:var(--teal);color:var(--white);font-size:16px;padding:10px 18px}

/* plans */
.plans{left:0;top:1872px;width:1200px}
.plan{top:2017px;width:226px;background:var(--white);box-shadow:0 3px 8px rgba(0,0,0,.28);text-align:center;padding-bottom:26px}
.plan-head{background:var(--blue);color:var(--white);padding:16px 0 12px;font-weight:700}
.plan-head .name{font-size:14px}
.plan-head .price{font-size:20px;margin-top:6px}
.plan-head .price small{font-size:13px}
.plan .speed{font-weight:700;font-size:17px;color:#333;padding:20px 30px 0;line-height:22px;height:74px}
.plan-icon{width:100px;height:100px;border-radius:50%;background:var(--blue);margin:12px auto 24px;display:flex;align-items:center;justify-content:center}
.plan-feature-title{font-weight:700;font-size:15px;line-height:19px;margin-top:8px}
.plan-feature-text{font-size:11.5px;color:#777;line-height:15px;padding:10px 22px 16px}

/* testimonial */
.testimonial{left:0;top:2542px;width:1200px;height:476px;background:var(--blue);color:var(--white);text-align:center}
.testimonial h2{font-family:"Hind",Arial,sans-serif;font-weight:500;font-size:40px;margin-top:48px}
.slider{display:flex;justify-content:center;align-items:center;gap:32px;margin-top:32px}
.arrow-btn{width:40px;height:34px;background:var(--teal);display:flex;align-items:center;justify-content:center}
.avatar{width:118px;height:118px;background:linear-gradient(160deg,#e8ecef,#b8a89a)}
.quote{position:relative;width:980px;margin:42px auto 0;font-size:15px;line-height:25px}
.quote-mark{position:absolute;left:-10px;top:-30px;font-family:Georgia,serif;font-size:80px;color:var(--teal)}
.client{color:var(--teal-light);font-size:20px;font-weight:600;margin-top:18px}

/* newsletter */
.news{left:0;top:3084px;width:1200px}
.subscribe{left:324px;top:3192px;display:flex}
.subscribe .field{width:482px;height:36px;border:1px solid #ccc;font-size:13px;color:#999;padding:9px 14px}
.subscribe .go{width:108px;height:36px;background:var(--blue);color:var(--white);font-size:14px;text-align:center;line-height:36px}

/* footer */
.footer{left:0;top:3302px;width:1200px;height:432px;background:var(--footer);color:#ccc}
.col{position:absolute;top:48px}
.col h4{color:var(--white);font-size:15px;font-weight:700;letter-spacing:.5px}
.col .bar{width:30px;height:2px;background:#555;margin:12px 0 20px}
.contact-row{display:flex;gap:14px;font-size:13px;margin-bottom:22px;line-height:18px}
.socials{display:flex;gap:10px}
.socials span{width:28px;height:28px;border-radius:50%;border:1px solid #666}
.news-item{margin-bottom:16px}
.news-item b{display:block;font-weight:400;color:#ddd;font-size:13px}
.news-item i{font-style:normal;font-size:10px;color:#888}
.about{font-size:12px;line-height:22px;color:#bbb}
.qc-field{width:232px;height:34px;background:#2a2a2a;color:#ddd;font-size:11px;padding:10px 12px;margin-bottom:8px}
.qc-msg{height:94px}
.send{display:inline-block;background:var(--teal);color:var(--white);font-size:18px;padding:8px 28px;margin-top:6px}
.copy{position:absolute;left:60px;right:60px;bottom:0;height:52px;border-top:1px solid #333;text-align:center;font-size:13px;line-height:52px;color:#ccc}
</style>
</head>
<body>

<header class="hero abs" role="img" aria-label="Office photo: smiling support agent with headset at a desk, colleagues behind">
</header>
<div class="logo-box abs"><span class="logo-mark"></span><span class="logo-name">Brightlink</span></div>
<nav class="nav-bar abs">
  <div class="nav-top">
    <span>&#9742; (555) 010-4274</span>
    <svg width="26" height="22" viewBox="0 0 26 22"><path d="M1 3h4l3 11h13l3-8H7" fill="none" stroke="#fff" stroke-width="2"/><circle cx="10" cy="19" r="2" fill="#fff"/><circle cx="19" cy="19" r="2" fill="#fff"/></svg>
    <span class="dot"></span><span class="dot"></span>
  </div>
  <div class="nav-links">
    <a class="active">HOME</a><a>WHY BRIGHTLINK</a><a>PLANS &amp; PACKAGES</a><a>MY ACCOUNT</a><a>GALLERY</a><a>CONTACTS</a>
    <span class="signup-btn"><svg width="14" height="14" viewBox="0 0 14 14"><circle cx="7" cy="4" r="3.5" fill="#fff"/><path d="M0 14c0-5 14-5 14 0z" fill="#fff"/></svg>Sign Up</span>
  </div>
</nav>
<div class="hero-box abs">
  <h1>FINALLY, THE INTERNET<br>YOU DESERVE IS HERE.</h1>
  <p>Affordable, reliable, high-speed internet is available locally right now</p>
</div>

<section class="why abs">
  <h2 class="section-title">WHY BRIGHTLINK</h2>
  <p class="section-sub">Brightlink is a company that provides Residential and Businesses access to the Internet and other related services such as VOIP and WiFi</p>
</section>
<div class="card abs" style="left:55px"><div class="card-photo" role="img" aria-label="Rooftop antenna against blue sky"></div><div class="card-label">Residential Internet Access</div><p>Brightlink's VOIP home phone solutions offer you a reliable, portable, low-cost alternative</p><span class="btn">READ MORE</span></div>
<div class="card abs" style="left:334px"><div class="card-photo" role="img" aria-label="Business meeting handshake" style="background:linear-gradient(180deg,#6c7b88,#a9a39b)"></div><div class="card-label">Business Internet Access</div><p>Choose from a variety of high-speed internet services that harness the power of the</p><span class="btn">READ MORE</span></div>
<div class="card abs" style="left:612px"><div class="card-photo" role="img" aria-label="Transmission towers against sky" style="background:linear-gradient(180deg,#9fc3e3,#5b87ad)"></div><div class="card-label">Unlimited Internet Usage</div><p>Brightlink offers high speed internet to meet your needs at an affordable price.</p><span class="btn">READ MORE</span></div>
<div class="card abs" style="left:891px"><div class="card-photo" role="img" aria-label="Wireless antenna on rooftop" style="background:linear-gradient(180deg,#2f6fc0,#8bb4e0 70%,#9a7a63)"></div><div class="card-label">Our Features</div><p>Brightlink's VOIP home phone solutions offer you a reliable, portable, low-cost alternative</p><span class="btn">READ MORE</span></div>

<div class="speed-photo abs" role="img" aria-label="Group of young people using phones and tablets at a table"></div>
<svg class="abs" style="left:112px;top:1450px" width="210" height="210" viewBox="0 0 210 210"><circle cx="105" cy="105" r="100" fill="none" stroke="#fff" stroke-width="5"/><rect x="78" y="55" width="54" height="96" rx="6" fill="none" stroke="#fff" stroke-width="5"/><circle cx="105" cy="138" r="5" fill="#fff"/></svg>
<section class="speed-panel abs">
  <h2>Fast download &amp; upload speeds<br>at an affordable price</h2>
  <div class="rule"></div>
  <p>When choosing among the best high speed Internet providers, there are several other factors that should be taken into consideration besides just the available download speeds.</p>
  <p>Upload speeds are important as well, though they probably are not as crucial as download speeds.</p>
  <div class="features">
    <div class="feature"><svg width="44" height="44" viewBox="0 0 44 44"><circle cx="22" cy="22" r="8" fill="none" stroke="#1d3f6e" stroke-width="2.5"/><circle cx="22" cy="22" r="16" fill="none" stroke="#1d3f6e" stroke-width="2.5" stroke-dasharray="6 4"/></svg>Customer<br>suport center</div>
    <div class="feature"><svg width="44" height="44" viewBox="0 0 44 44"><circle cx="22" cy="22" r="18" fill="none" stroke="#1d3f6e" stroke-width="2.5"/><circle cx="22" cy="18" r="5" fill="none" stroke="#1d3f6e" stroke-width="2.5"/><path d="M13 32c2-7 16-7 18 0" fill="none" stroke="#1d3f6e" stroke-width="2.5"/></svg>Equipment<br>Options</div>
    <div class="feature"><svg width="44" height="44" viewBox="0 0 44 44"><path d="M22 3l5.6 12 13 1.4-9.8 8.8 2.8 12.8L22 31.5 10.4 38l2.8-12.8L3.4 16.4l13-1.4z" fill="none" stroke="#1d3f6e" stroke-width="2.5"/></svg>Customer<br>guarantee</div>
  </div>
  <span class="speed-btn">Find Your Best Deals in Your Area</span>
</section>

<section class="plans abs">
  <h2 class="section-title" style="letter-spacing:0">Plan and Packages</h2>
  <p class="section-sub">You can order these Plans and Packages here</p>
</section>
<div class="plan abs" style="left:55px">
  <div class="plan-head"><div class="name">BRIGHTLINK SIMPLICITY</div><div class="price">$39.99 <small>MO/1YR</small></div></div>
  <div class="speed">5 MB DOWNLOAD SPEED</div>
  <div class="plan-icon"><svg width="50" height="50" viewBox="0 0 50 50"><rect x="8" y="28" width="34" height="10" rx="2" fill="#fff"/><line x1="25" y1="28" x2="25" y2="14" stroke="#fff" stroke-width="3"/><path d="M17 14a11 11 0 0 1 16 0" fill="none" stroke="#fff" stroke-width="3"/></svg></div>
  <span class="btn">SIGN UP</span>
</div>
<div class="plan abs" style="left:344px">
  <div class="plan-head"><div class="name">BRIGHTLINK SPEED</div><div class="price">$89.99 <small>MO/1YR</small></div></div>
  <div class="speed">50 MB DOWNLOAD SPEED</div>
  <svg width="44" height="48" viewBox="0 0 44 48"><path d="M22 4v28M10 20l12 12 12-12" fill="none" stroke="#1bb1cc" stroke-width="3.5"/><line x1="6" y1="44" x2="38" y2="44" stroke="#1bb1cc" stroke-width="3.5"/></svg>
  <div class="plan-feature-title">Super Fast<br>Download Speed</div>
  <div class="plan-feature-text">When shopping for internet access, people usually look for what is reliable, fast and affordable</div>
  <span class="btn">SIGN UP</span>
</div>
<div class="plan abs" style="left:627px">
  <div class="plan-head"><div class="name">BRIGHTLINK VALUE PAK</div><div class="price">$45.95 <small>MO/1YR</small></div></div>
  <div class="speed">10 MB DOWNLOAD SPEED</div>
  <div class="plan-icon"><svg width="56" height="50" viewBox="0 0 56 50"><circle cx="28" cy="25" r="6" fill="#fff"/><path d="M18 15a14 14 0 0 0 0 20M38 15a14 14 0 0 1 0 20M11 8a24 24 0 0 0 0 34M45 8a24 24 0 0 1 0 34" fill="none" stroke="#fff" stroke-width="3.5"/></svg></div>
  <span class="btn">SIGN UP</span>
</div>
<div class="plan abs" style="left:911px">
  <div class="plan-head"><div class="name">BRIGHTLINK SUPER PAK</div><div class="price">$69.99 <small>MO/1YR</small></div></div>
  <div class="speed">25 MB DOWNLOAD SPEED</div>
  <div class="plan-icon"><svg width="56" height="56" viewBox="0 0 56 56"><circle cx="28" cy="20" r="4" fill="#fff"/><path d="M28 22l-7 26M28 22l7 26M20 12a12 12 0 0 0 0 16M36 12a12 12 0 0 1 0 16" fill="none" stroke="#fff" stroke-width="3"/></svg></div>
  <span class="btn">SIGN UP</span>
</div>

<section class="testimonial abs">
  <h2>What Our Clients Have to Say</h2>
  <div class="slider">
    <span class="arrow-btn"><svg width="18" height="14" viewBox="0 0 18 14"><path d="M0 7h16M10 1l6 6-6 6" fill="none" stroke="#fff" stroke-width="2.5"/></svg></span>
    <div class="avatar" role="img" aria-label="Client portrait"></div>
    <span class="arrow-btn"><svg width="18" height="14" viewBox="0 0 18 14"><path d="M18 7H2M8 1L2 7l6 6" fill="none" stroke="#fff" stroke-width="2.5"/></svg></span>
  </div>
  <div class="quote"><span class="quote-mark">&ldquo;</span>We are pleased to say that work done by this company is outstanding. Everything what we asked was done on time and with high precision by the professional team. With proper briefing there is no room for any mistakes. During the project execution team has applied requested changes in professional manner.</div>
  <div class="client">-Dana Ruiz</div>
</section>

<section class="news abs">
  <h2 class="section-title" style="letter-spacing:0;font-size:38px">Signup Below to Get News</h2>
  <p class="section-sub" style="margin-top:0">Subscribe to our mailing list</p>
</section>
<div class="subscribe abs"><div class="field">Your Email</div><div class="go">Subscribe</div></div>

<footer class="footer abs">
  <div class="col" style="left:70px">
    <h4>CONTACTS</h4><div class="bar"></div>
    <div class="contact-row"><span>&#9742;</span>(555) 123 45 67</div>
    <div class="contact-row"><span>&#9993;</span>info@brightlinknet.nyc</div>
    <div class="contact-row"><svg width="12" height="16" viewBox="0 0 12 16"><path d="M6 0a6 6 0 0 1 6 6c0 4-6 10-6 10S0 10 0 6a6 6 0 0 1 6-6z" fill="#ccc"/><circle cx="6" cy="6" r="2" fill="#1c1c1c"/></svg><span>48 Harbor Lane, Brooklyn, New York<br>11201, USA</span></div>
    <div class="socials"><span></span><span></span><span></span><span></span><span></span><span></span></div>
  </div>
  <div class="col" style="left:344px">
    <h4>LATEST NEWS</h4><div class="bar"></div>
    <div class="news-item"><b>This is a Audio post Type</b><i>January 6, 2016</i></div>
    <div class="news-item"><b>This is a Gallery post Type</b><i>January 6, 2016</i></div>
    <div class="news-item"><b>This is a Quote post Type</b><i>January 6, 2016</i></div>
    <div class="news-item"><b>Post Video</b><i>October 2, 2015</i></div>
  </div>
  <div class="col" style="left:585px;width:250px">
    <h4>ABOUT</h4><div class="bar"></div>
    <p class="about">Cum sociis natoque penatibus et magnis dis parturient montes, nascetur ridiculus mus. Etiam imperdiet. Ut sollicitudin sem sit amet ipsum. In id dui. Pellentesque sapien. Curabitur commodo elit eget erat. Aliquam sit amet nibh. Ut ornare elit. Donec ac nisi eget.</p>
  </div>
  <div class="col" style="left:884px">
    <h4>QUICK CONTACT</h4><div class="bar"></div>
    <div class="qc-field">YOUR NAME</div>
    <div class="qc-field">YOUR EMAIL</div>
    <div class="qc-field qc-msg">MESSAGE...</div>
    <span class="send">Send</span>
  </div>
  <div class="copy">© 2016 Brightlinknet.nyc Right Reserved.</div>
</footer>

</body>
</html>
```